New business card/stationary for a consulting company

I am looking for a clean and very professional looking business card for my consulting company as well as corresponding stationary. I am uploading our logo. I like simple and powerful for the feel. No graphics but I am open on everything else. Below is my contact information but would like the final to be in a version I can add my employees information into and print. Thank you.

Daniel Whitcombe
dan@ferncrestadvisory.com
2738 North 17th Avenue, Summit Floor, Oak Brook, Illinois 60126
www.ferncrestadvisory.com

Industry/Entity Type

Consulting

Contact Information for Business Card

Daniel Whitcombe
dan@ferncrestadvisory.com
www.ferncrestadvisory.com

Font styles to use
Serif
Sans Serif

Requirements
Must have
• Our logo and the business card details.
Nice to have
• our website www.ferncrestadvisory.com

```html
<!DOCTYPE html>
<html lang="en">
<head>
<meta charset="utf-8">
<title>Ferncrest Advisory – Business Card</title>
<link rel="stylesheet" href="https://fonts.googleapis.com/css2?family=Open+Sans:wght@400;700&display=swap">
<style>
  :root {
    --navy: #1f1b6e;
    --ink-grey: #5a5a5a;
    --rule-grey: #6f6f6f;
    --card: #ffffff;
    --backdrop: #e4e5e7;
  }
  * { margin: 0; padding: 0; box-sizing: border-box; }
  html, body {
    width: 1200px; height: 904px; overflow: hidden;
    background: var(--backdrop);
    font-family: "Open Sans", Arial, sans-serif;
  }
  .stage {
    width: 1200px; height: 904px;
    display: flex; flex-direction: column; align-items: center; justify-content: center;
    gap: 44px;
  }
  .card {
    position: relative;
    width: 620px; height: 354px;
    background: var(--card);
    box-shadow: 0 6px 18px rgba(0,0,0,0.18);
  }
  /* front */
  .card-front { display: flex; align-items: center; justify-content: center; }
  .brand { display: flex; align-items: center; gap: 10px; color: var(--navy); white-space: nowrap; }
  .brand-square { width: 22px; height: 22px; background: var(--navy); }
  .brand-name {
    font-weight: 400; font-size: 24px; letter-spacing: 2px; text-transform: uppercase;
  }
  /* back */
  .card-back .brand { position: absolute; left: 62px; top: 104px; gap: 9px; }
  .card-back .brand-square { width: 18px; height: 18px; }
  .card-back .brand-name { font-size: 18px; letter-spacing: 1.5px; }
  .holder {
    position: absolute; right: 26px; top: 56px;
    font-weight: 700; font-size: 18px; color: var(--navy);
  }
  .holder-rule {
    position: absolute; left: 340px; right: 16px; top: 88px;
    height: 1px; background: var(--rule-grey);
  }
  .address-rule {
    position: absolute; left: 0; width: 262px; top: 234px;
    height: 1px; background: var(--rule-grey);
  }
  .address {
    position: absolute; left: 38px; top: 244px;
    font-size: 13.5px; line-height: 1.45; color: var(--ink-grey);
    font-style: normal;
  }
  .divider {
    position: absolute; left: 276px; top: 180px; width: 1px; height: 78px;
    background: var(--rule-grey);
  }
  .contact {
    position: absolute; left: 292px; top: 182px;
    list-style: none; font-size: 13.5px; color: var(--ink-grey);
  }
  .contact li { display: flex; align-items: center; gap: 8px; height: 22px; }
  .contact svg { width: 14px; height: 14px; flex: none; }
</style>
</head>
<body>
<main class="stage">
  <section class="card card-front" aria-label="Card front">
    <div class="brand">
      <span class="brand-square"></span>
      <span class="brand-name">Ferncrest Advisory</span>
    </div>
  </section>

  <section class="card card-back" aria-label="Card back">
    <div class="brand">
      <span class="brand-square"></span>
      <span class="brand-name">Ferncrest Advisory</span>
    </div>

    <p class="holder">Daniel Whitcombe</p>
    <div class="holder-rule"></div>

    <ul class="contact">
      <li>
        <svg viewBox="0 0 14 14" aria-hidden="true">
          <circle cx="7" cy="7" r="7" fill="var(--navy)"/>
          <rect x="3.3" y="4.5" width="7.4" height="5" fill="none" stroke="#fff" stroke-width="1"/>
          <polyline points="3.3,4.5 7,7.4 10.7,4.5" fill="none" stroke="#fff" stroke-width="1"/>
        </svg>
        dan@ferncrestadvisory.com
      </li>
      <li>
        <svg viewBox="0 0 14 14" aria-hidden="true">
          <circle cx="7" cy="7" r="7" fill="var(--navy)"/>
          <circle cx="7" cy="7" r="4" fill="none" stroke="#fff" stroke-width="0.9"/>
          <ellipse cx="7" cy="7" rx="1.7" ry="4" fill="none" stroke="#fff" stroke-width="0.9"/>
          <line x1="3" y1="7" x2="11" y2="7" stroke="#fff" stroke-width="0.9"/>
        </svg>
        www.ferncrestadvisory.com
      </li>
    </ul>
    <div class="divider"></div>

    <div class="address-rule"></div>
    <address class="address">
      2738 North 17th Avenue<br>
      Summit Floor, Cedar Ridge<br>
      Illinois 60140
    </address>
  </section>
</main>
</body>
</html>
```